IT Management and Consulting company wants a design

The website should transfer an innovative, forward-oriented, optimistic, and serious image to my customer. Because we work in an agile, the design should transfer this approach.

The new color should make a serious, but not boring, impression for the business visitors of top-level companies.

The main focus topics are:
* IT strategy consulting
* Digital transformation
* IT quality management

The website should be in the English language.

The website should be created for WordPress. The existing website is http://www.t-vork.com (no WordPress) is provided by servalpin.de. A WordPress sandbox system exists.

Target Market(s)

Purchasing departments, IT decision makers from companies, project recruiting companies

Industry/Entity Type

IT-Provider, Telecommunication, Automotive

Coding

Coded - Design and coding required

Number of Pages Required

4 page

Font styles to use
Serif
Sans Serif

Requirements
Must have
• Long-pager scrolling, a detail page for each portfolio topics, contact page, page about the company
Nice to have
• Parallax animation less is more, maybe a nice Hero Video Header, interessting 3D graph, Isometric graphs will bi nice, more clean than overloaded,
Should not have
• personal recruting page like in www.t-vork.com

```html
<!DOCTYPE html>
<html lang="en">
<head>
<meta charset="utf-8">
<title>Talvork Consulting</title>
<link rel="stylesheet" href="https://fonts.googleapis.com/css2?family=Montserrat:wght@500;600&family=Roboto:wght@400;500&display=swap">
<style>
:root{
  --gold:#b87c03;
  --gold-light:#d9b56a;
  --ink:#1a1a1a;
  --text:#333;
  --soft:#f4f4f4;
  --white:#fff;
  --black:#000;
}
*{box-sizing:border-box;margin:0;padding:0}
html,body{width:1200px;height:3627px;overflow:hidden}
body{position:relative;background:var(--white);font-family:'Roboto',sans-serif;color:var(--text);font-size:15px;line-height:1.7}
.abs{position:absolute}
h1,h2,h3,h4{font-family:'Montserrat',sans-serif;font-weight:500;color:var(--ink)}
.btn{position:absolute;display:flex;align-items:center;justify-content:center;gap:8px;height:37px;border-radius:19px;background:var(--gold);color:var(--white);font-family:'Montserrat',sans-serif;font-weight:600;font-size:14px;letter-spacing:.2px}
.btn svg{width:14px;height:14px}
.logo{position:absolute;display:flex;align-items:center;gap:8px;font-family:'Roboto',sans-serif;font-weight:500;font-size:18px;color:var(--gold);z-index:2}
.logo-mark{width:10px;height:10px;background:var(--gold)}
/* header */
.hero-shape{top:0;left:598px;z-index:0}
.nav{position:absolute;top:22px;left:409px;display:flex;gap:30px;font-size:15px;color:var(--ink);z-index:2}
.lang{position:absolute;top:22px;left:927px;display:flex;align-items:center;gap:4px;font-size:14px;font-weight:500;color:var(--gold);z-index:2}
.login{position:absolute;top:17px;left:993px;width:96px;height:37px;border-radius:19px;background:var(--white);box-shadow:0 2px 8px rgba(0,0,0,.18);display:flex;align-items:center;justify-content:center;font-family:'Montserrat',sans-serif;font-weight:600;font-size:14px;color:var(--ink);z-index:2}
.hero-title{top:270px;left:110px;font-size:42px;line-height:51px;letter-spacing:.5px;z-index:1}
.hero-text{top:382px;left:111px;width:430px;font-size:15px;line-height:26px;z-index:1}
/* services */
.section-title{width:1200px;text-align:center;font-size:29px}
.section-lead{width:1200px;text-align:center;font-size:15px;line-height:26px}
.card{position:absolute;top:894px;width:306px;height:237px;padding:25px 24px}
.card.active{background:var(--white);border-radius:18px;box-shadow:0 2px 14px rgba(0,0,0,.12)}
.card-icon{width:55px;height:55px;border-radius:7px;background:var(--gold);display:flex;align-items:center;justify-content:center}
.card h3{margin-top:12px;font-size:20px}
.card p{margin-top:4px;font-size:15px;line-height:26px}
/* about */
.about{top:1214px;left:0;width:1200px;height:388px;background:var(--gold);color:var(--white);text-align:center}
.about h2{color:var(--white);font-size:29px;margin-top:60px}
.about p{font-size:15px;line-height:26px;margin:0 auto}
.btn.outline{background:transparent;border:2px solid var(--white)}
/* feature blocks */
.feature-title{font-size:29px;color:var(--gold)}
.feature-text{font-size:15px;line-height:26px;width:500px}
/* contact */
.contact{top:2608px;left:0;width:1200px;height:598px;background:var(--soft)}
.field{position:absolute;border-bottom:1px solid #777;font-size:15px;color:var(--ink)}
.field span{display:block}
/* footer */
.footer{top:3206px;left:0;width:1200px;height:421px;background:var(--black);color:var(--white)}
.footer h4{position:absolute;color:var(--white);font-size:19px;top:117px}
.footer ul{position:absolute;list-style:none;top:150px;font-size:15px;line-height:30px}
.social{position:absolute;top:162px;left:934px;display:flex;gap:10px}
.social span{width:30px;height:30px;border-radius:50%;background:var(--gold)}
.contact-line{position:absolute;left:711px;display:flex;gap:10px;font-size:15px}
.contact-line svg{width:14px;height:14px;margin-top:4px;flex:none}
</style>
</head>
<body>

<!-- hero shape sits behind header -->
<svg class="abs hero-shape" width="602" height="580" viewBox="0 0 602 580" role="img" aria-label="Photo of two colleagues discussing work at a laptop">
  <defs><linearGradient id="heroFill" x1="0" y1="0" x2="1" y2="1"><stop offset="0" stop-color="#e2c98d"/><stop offset=".6" stop-color="#c9a35a"/><stop offset="1" stop-color="#9c7a3a"/></linearGradient></defs>
  <path d="M270 0 H602 V440 C520 500 420 600 300 575 C160 550 20 460 2 300 C-12 180 120 80 270 0 Z" fill="url(#heroFill)"/>
</svg>

<!-- header -->
<div class="logo" style="top:22px;left:113px"><span class="logo-mark"></span>Talvork Consulting</div>
<nav class="nav"><span>Home</span><span>About Us</span><span>Services</span><span>Portfolio</span><span>Scouting</span><span>contact</span></nav>
<div class="lang">EN <svg width="12" height="12" viewBox="0 0 12 12"><path d="M2 4l4 4 4-4" stroke="#b87c03" stroke-width="2" fill="none"/></svg></div>
<div class="login">LOG IN</div>

<!-- hero -->
<h1 class="abs hero-title">WELCOME TO<br>TALVORK CONSULTING</h1>
<p class="abs hero-text">Our mission is to carry out complex projects efficiently with high quality for the benefit of our customers.</p>
<div class="btn" style="top:454px;left:113px;width:166px">GET STARTED
  <svg viewBox="0 0 14 14"><circle cx="7" cy="7" r="7" fill="#fff"/><path d="M5 4l3 3-3 3" stroke="#b87c03" stroke-width="1.8" fill="none"/></svg></div>

<!-- services -->
<h2 class="abs section-title" style="top:720px;left:0">OUR SERVICES</h2>
<p class="abs section-lead" style="top:780px;left:0">Lorem ipsum dolor sit amet, consectetur adipiscing elit, sed do eiusmod tempor incididunt enim<br>ad minim veniam, quis nostrud exercitation ullamco laboris nisi ut aliquip</p>

<div class="card" style="left:110px">
  <div class="card-icon"><svg width="32" height="32" viewBox="0 0 32 32" fill="none" stroke="#fff" stroke-width="2"><circle cx="10" cy="7" r="3"/><path d="M10 11v10M10 21l-4 8M10 21l4 8M18 4h10v8H18"/></svg></div>
  <h3>IT Strategy Consulting</h3>
  <p>Lorem ipsum dolor sit amet, consectetur adipiscing elit, sed do eiusmod tempor incididunt ut labore et dolore magna aliqua.</p>
</div>
<div class="card active" style="left:446px">
  <div class="card-icon"><svg width="32" height="32" viewBox="0 0 32 32" fill="none" stroke="#fff" stroke-width="2"><circle cx="14" cy="16" r="8"/><circle cx="14" cy="16" r="3"/><path d="M22 10h6M22 16h6M22 22h6"/></svg></div>
  <h3>Digital Transformation</h3>
  <p>Lorem ipsum dolor sit amet, consectetur adipiscing elit, sed do eiusmod tempor incididunt ut labore et dolore magna aliqua.</p>
</div>
<div class="card" style="left:782px">
  <div class="card-icon"><svg width="32" height="32" viewBox="0 0 32 32" fill="none" stroke="#fff" stroke-width="2"><circle cx="16" cy="16" r="9" stroke-dasharray="4 2.5"/><circle cx="16" cy="16" r="6"/><path d="M13 16l2 2 4-4"/></svg></div>
  <h3>IT Quality Management</h3>
  <p>Lorem ipsum dolor sit amet, consectetur adipiscing elit, sed do eiusmod tempor incididunt ut labore et dolore magna aliqua.</p>
</div>

<!-- about -->
<section class="abs about">
  <h2>ABOUT US</h2>
  <p style="margin-top:12px;width:560px">Our mission is to carry out complex projects efficiently with high quality for the benefit of our customers. - Transparent, reliable, agile</p>
  <p style="margin-top:19px;width:880px">A deliberately high standard for which we bundle all the qualities that are important to meet them. For example, in-depth methodological and IT competence as well as many years of experience in projects throughout the entire development process - supplemented by the ability to constructively involve all those involved.</p>
  <div class="btn outline" style="top:286px;left:491px;width:156px">READ MORE
    <svg viewBox="0 0 14 14"><circle cx="7" cy="7" r="7" fill="#fff"/><path d="M5 4l3 3-3 3" stroke="#b87c03" stroke-width="1.8" fill="none"/></svg></div>
</section>

<!-- portfolio -->
<svg class="abs" style="top:1690px;left:110px" width="402" height="408" viewBox="0 0 402 408" role="img" aria-label="Photo of a team meeting with colleagues seated in a circle">
  <defs><linearGradient id="portFill" x1="0" y1="0" x2="1" y2="1"><stop offset="0" stop-color="#d8d6d2"/><stop offset=".5" stop-color="#9a8f86"/><stop offset="1" stop-color="#5b5450"/></linearGradient></defs>
  <path d="M230 0 C330 0 400 60 402 150 C404 260 330 400 230 408 C130 414 20 330 2 250 C-10 190 80 130 140 60 C170 25 195 0 230 0 Z" fill="url(#portFill)"/>
</svg>
<h2 class="abs feature-title" style="top:1718px;left:570px">PORTFOLIO</h2>
<p class="abs feature-text" style="top:1770px;left:573px">Our range of services covers the management of the entire development process from applications and extensions to quality assurance through to going live and support afterwards.Talvork Consulting specializes in complex projects in heterogeneous IT environments. We deliver in high quality. We work with the necessary procedural models to achieve customer satisfaction and project success.</p>
<div class="btn" style="top:1952px;left:573px;width:154px">READ MORE
  <svg viewBox="0 0 14 14"><circle cx="7" cy="7" r="7" fill="#fff"/><path d="M5 4l3 3-3 3" stroke="#b87c03" stroke-width="1.8" fill="none"/></svg></div>

<!-- scouting -->
<h2 class="abs feature-title" style="top:2197px;left:112px">SCOUTING</h2>
<p class="abs feature-text" style="top:2250px;left:112px;width:470px">Are you looking for a company with an unusually large scope for development - whether permanent or free? Talvork Consulting offers a lot of space for people with ideas and drive. If you also like the idea of helping to shape an expanding company in close contact with the management, we look forward to hearing from you!</p>
<div class="btn" style="top:2403px;left:111px;width:154px">READ MORE
  <svg viewBox="0 0 14 14"><circle cx="7" cy="7" r="7" fill="#fff"/><path d="M5 4l3 3-3 3" stroke="#b87c03" stroke-width="1.8" fill="none"/></svg></div>
<svg class="abs" style="top:2119px;left:684px" width="403" height="406" viewBox="0 0 403 406" role="img" aria-label="Photo of a group of colleagues talking around a meeting table">
  <defs><linearGradient id="scoutFill" x1="0" y1="0" x2="1" y2="1"><stop offset="0" stop-color="#b7a99a"/><stop offset=".5" stop-color="#6d6258"/><stop offset="1" stop-color="#3a3836"/></linearGradient></defs>
  <path d="M240 0 C330 0 403 70 403 160 C403 270 320 400 210 406 C110 410 0 330 0 230 C0 160 70 110 130 50 C165 15 200 0 240 0 Z" fill="url(#scoutFill)"/>
</svg>

<!-- contact -->
<section class="abs contact">
  <h2 class="abs section-title" style="top:40px;left:0;color:var(--gold)">Get In Touch With US</h2>
  <p class="abs section-lead" style="top:92px;left:0">Lorem ipsum dolor sit amet, consectetur adipiscing elit</p>
  <div class="field" style="top:187px;left:165px;width:367px;height:55px"><span>Name</span><span>| Frist name</span></div>
  <div class="field" style="top:189px;left:647px;width:367px;height:55px"><span>Email Address</span><span>@anymail.com</span></div>
  <div class="field" style="top:290px;left:165px;width:367px;height:55px"><span>Phone</span><span>987 654 3210</span></div>
  <div class="field" style="top:290px;left:651px;width:367px;height:55px"><span>Subject</span><span>Lorem ipsum</span></div>
  <div class="field" style="top:396px;left:165px;width:871px;height:67px"><span>Message</span><span style="margin-top:5px">Lorem ipsum dolor</span></div>
  <div class="btn" style="top:514px;left:549px;width:116px">SUBMIT</div>
</section>

<!-- footer -->
<footer class="abs footer">
  <div class="logo" style="top:108px;left:110px"><span class="logo-mark"></span>Talvork Consulting</div>
  <p class="abs" style="top:164px;left:110px;width:210px;font-size:15px;line-height:22px">Lorem ipsum dolor sit amet, consectetur adipiscing elitLorem ipsum dolor sit elit</p>

  <h4 style="left:366px">Using Link</h4>
  <ul style="left:368px"><li>Home</li><li>About Us</li><li>Services</li><li>Portfolio</li><li>Scouting</li><li>contact</li></ul>

  <h4 style="left:529px">Help Link</h4>
  <ul style="left:531px"><li>Terms&amp;condtions</li><li>Privacy Policy</li><li>Support</li></ul>

  <h4 style="left:711px">Contact Us</h4>
  <div class="contact-line" style="top:148px"><svg viewBox="0 0 14 14"><path d="M3 1l2 3-1.5 1.5c.8 2 2.2 3.4 4 4L9 8l3 2-1 3C6 13 1 8 1 3z" fill="#b87c03"/></svg>987 654 321</div>
  <div class="contact-line" style="top:193px"><svg viewBox="0 0 14 14" fill="none" stroke="#b87c03" stroke-width="1.4"><rect x="1" y="3" width="12" height="9"/><path d="M1 3l6 5 6-5"/></svg>info@talvork.com</div>
  <div class="contact-line" style="top:241px;line-height:36px"><svg viewBox="0 0 14 14"><path d="M7 1a4 4 0 0 1 4 4c0 3-4 8-4 8S3 8 3 5a4 4 0 0 1 4-4z" fill="#b87c03"/><circle cx="7" cy="5" r="1.5" fill="#000"/></svg><span style="margin-top:-8px">250Lorem ipsum dolor sit<br>amet 2003</span></div>

  <h4 style="left:934px">Follow Us</h4>
  <div class="social"><span></span><span></span><span></span><span></span></div>

  <p class="abs" style="top:354px;left:0;width:1200px;text-align:center;font-size:15px">©Copyrights 2021 &nbsp;talvork consulting | &nbsp;&nbsp;All Rights Reserved</p>
  <p class="abs" style="top:358px;left:1127px;font-size:11px">C49</p>
</footer>

</body>
</html>
```